Ice Cream Cup Design

We need a packaging design for ice cream cups.
We're a London based company called Villa Rosa Dolci and are producers of fresh Italian Artisan Gelato our website is www.villarosadolci.co.uk

We're looking to invest in a cup filling machine to fill 100ml and 500ml cups of gelato.
The 500ml cup will be the same shape and height as the Nordvik Freeze tub with a matching lid design.
The 100ml cup will be of the same shape and height of the Nordvik Freeze Single Serve cup with a matching lid design and includes a spoon inside.

We're looking for edgy clean designs that give an impression of quality and draw attention to the product if it sat on a product shelf. Inspired by packaging such as Ko, Pemberly and Harrowfield we're keen on a black themed packaging with a striking contrast of simple colour and a simple ice cream or gelato image that shows more than one flavour.
This particular design is not boasting any particular flavour, its a uniform design across our whole range of flavours.

Our company logo may be too fussy for this packaging so we would like to include our company ice cream logo and a way to include our company name but still look edgy for example - just like Pemberly Tea - our ice cream logo big G underneath, then 'VILLA ROSA DOLCI' underneath, and below that 'ARTISAN ITALIAN GELATO'. Or anything that inspires and looks good, will draw attention and looks sexy and indulgent and gives an impression of luxury product.

Please check attached document for cup shape and dimensions.

Reason: Christmas and New Year Holiday period resulted in less time for feedback opportunity and new designs to be posted.

Target Market(s)

Target market between 20-40 years old, consumers of quality desserts all year round.

Industry/Entity Type

It Company

Requirements
Must have
• Our Ice Cream Logo
Our name (doesn't need to necessarily have it in our font, can be in bold lettering)
Nice to have
• Limited writing and fuss.
Ideal to have simple clean designs
Should not have
• Eccentric colours and fun childlike images.

```html
<!DOCTYPE html>
<html lang="en">
<head>
<meta charset="utf-8">
<title>Villa Rosa Dolci – 500ml Gelato Tub</title>
<link rel="stylesheet" href="https://fonts.googleapis.com/css2?family=Roboto+Condensed:wght@300;400;700&display=swap">
<style>
  :root {
    --bg: #ececec;
    --wrap-black: #1c1c1c;
    --pattern-black: #262626;
    --gold: #f2c200;
    --gold-deep: #e0ad00;
    --white: #ffffff;
    --photo-dark: #3a1f14;
    --photo-mid: #6b3a22;
    --photo-light: #e89a3a;
  }
  * { margin: 0; padding: 0; box-sizing: border-box; }
  html, body {
    width: 1200px; height: 900px; overflow: hidden;
    background: var(--bg);
    font-family: "Roboto Condensed", Arial, sans-serif;
  }
  .canvas { position: relative; width: 1200px; height: 900px; }

  /* Lid */
  .lid { position: absolute; left: 50px; top: 270px; width: 340px; height: 340px; }

  /* Cup wrap, laid flat */
  .wrap {
    position: absolute; left: 440px; top: 150px;
    width: 700px; height: 600px;
    background: var(--wrap-black);
    overflow: hidden;
  }
  .wrap-pattern {
    position: absolute; left: 0; top: 0; width: 100%; height: 150px;
    background: linear-gradient(180deg, var(--pattern-black), var(--wrap-black));
  }
  .brand-small {
    position: absolute; left: 0; right: 0; top: 62px;
    text-align: center; color: var(--white);
    font-size: 15px; font-weight: 400; letter-spacing: 1px;
  }
  .brand-mark {
    position: absolute; left: 60px; top: 170px;
    width: 150px; height: 150px; border-radius: 50%;
    background: var(--gold);
  }
  .brand-name {
    position: absolute; left: 240px; top: 180px;
    color: var(--white); line-height: 0.95;
  }
  .brand-name .line-1 { display: block; font-size: 64px; font-weight: 700; }
  .brand-name .line-2 { display: block; font-size: 64px; font-weight: 400; }
  .brand-tagline {
    position: absolute; left: 240px; top: 318px;
    color: var(--gold); font-size: 30px; font-weight: 700; letter-spacing: 0.5px;
    line-height: 1.1; white-space: nowrap;
  }
  .band {
    position: absolute; left: 0; bottom: 0; width: 100%; height: 150px;
    background: var(--gold);
  }
  .band-icon {
    position: absolute; left: 48px; top: 26px; width: 46px; height: 46px;
    border-radius: 50%; background: var(--gold-deep);
  }
  .band-slogan {
    position: absolute; left: 118px; top: 22px;
    color: var(--white); font-size: 20px; font-weight: 400; line-height: 1.1;
  }
  .band-rule {
    position: absolute; left: 118px; top: 78px; width: 190px; height: 2px;
    background: var(--white);
  }
  .band-volume {
    position: absolute; left: 118px; top: 88px;
    color: var(--white); font-size: 30px; font-weight: 700;
  }
  .product-photo {
    position: absolute; right: 30px; bottom: 20px;
    width: 290px; height: 190px; border-radius: 10px;
    background: radial-gradient(circle at 40% 45%, var(--photo-mid), var(--photo-dark) 60%, var(--photo-light) 100%);
  }
</style>
</head>
<body>
<main class="canvas">

  <svg class="lid" viewBox="0 0 340 340" role="img" aria-label="Tub lid with brand name">
    <defs>
      <path id="rim-path" d="M170,170 m-150,0 a150,150 0 1,1 300,0 a150,150 0 1,1 -300,0"/>
    </defs>
    <circle cx="170" cy="170" r="168" fill="var(--gold)"/>
    <circle cx="170" cy="170" r="128" fill="var(--wrap-black)"/>
    <text font-family="Roboto Condensed, Arial, sans-serif" font-size="17" fill="var(--white)" letter-spacing="1">
      <textPath href="#rim-path">HOUSE OF ITALIAN ICECREAM – ARTISAN ITALIAN GELATO – HOUSE OF ITALIAN ICECREAM –</textPath>
    </text>
    <circle cx="112" cy="170" r="38" fill="var(--gold)"/>
    <text x="162" y="164" font-family="Roboto Condensed, Arial, sans-serif" font-size="22" font-weight="700" fill="var(--white)">VILLA ROSA</text>
    <text x="162" y="188" font-family="Roboto Condensed, Arial, sans-serif" font-size="22" font-weight="400" fill="var(--white)">DOLCI</text>
    <text x="162" y="206" font-family="Roboto Condensed, Arial, sans-serif" font-size="11" font-weight="700" fill="var(--gold)">ARTISAN ITALIAN GELATO</text>
  </svg>

  <section class="wrap">
    <div class="wrap-pattern" role="img" aria-label="Faint dark ornamental pattern"></div>
    <div class="brand-small">Villa Rosa Dolci</div>

    <div class="brand-mark"></div>
    <h1 class="brand-name">
      <span class="line-1">VILLA ROSA</span>
      <span class="line-2">DOLCI</span>
    </h1>
    <p class="brand-tagline">ARTISAN ITALIAN GELATO</p>

    <div class="band">
      <div class="band-icon"></div>
      <p class="band-slogan">THE HOUSE OF<br>ITALIAN ICE CREAM</p>
      <div class="band-rule"></div>
      <p class="band-volume">500ML</p>
    </div>

    <div class="product-photo" role="img" aria-label="Photo of chocolate and vanilla gelato scoops with orange pieces on a white plate"></div>
  </section>

</main>
</body>
</html>
```